A new home page for Brelvox!

Brelvox needs a needs a new home page. Something fresh, engaging and encompassing of the services and features of the brelvox product.

The product competitors are tarnu.com, quibfrosted.com, zumbek metrics

Hi there,

I'm on leave until Wednesday, so I'll look at all the designs and post comments.

Thank you!

Reason: Quantity of submissions and I was on business trip.

Target Market(s)

Anyone with a website that wants to track visitors, use live chat, support, 'hello' like bars, etc.

Industry/Entity Type

Zumbek

Font styles to use
Sans Serif

Colors

Designer to choose colors to be used in the design.

Requirements
Must have
• the home page must showcase somehow the product line, which is
Analytics
SEO
Live Chat
Support Tickets
Heat Maps
Tolvix (like plankrim)

visit brelvox.com for a full feature list.

```html
<!DOCTYPE html>
<html lang="en">
<head>
<meta charset="utf-8">
<title>Brelvox! — Website analytics and SEO tools</title>
<link href="https://fonts.googleapis.com/css2?family=Ubuntu:wght@300;400;500&family=Crimson+Text&display=swap" rel="stylesheet">
<style>
:root{
  --green:#3f8f2f;
  --green-dark:#2f6f23;
  --ink:#3a3a3a;
  --muted:#5b5b5b;
  --soft:#eeeeee;
  --line:#cfcfcf;
  --dark:#2a2a2a;
}
*{box-sizing:border-box;margin:0;padding:0}
html,body{width:812px;height:1200px;overflow:hidden;background:#fff}
body{position:relative;font-family:"Ubuntu",sans-serif;color:var(--ink)}
.abs{position:absolute}
.promo-bar{left:0;top:0;width:812px;height:31px;background:linear-gradient(#4f9a3a,#3d8129);color:#fff;font-size:10px;text-align:center;line-height:31px}
.promo-bar b{color:#f3e04a;font-weight:400}
.promo-close{right:9px;top:8px;width:14px;height:14px;border-radius:50%;background:#1f3d17;color:#fff;font-size:9px;line-height:14px;text-align:center}
.site-header{left:0;top:31px;width:812px;height:61px;background:#fff}
.brand{left:69px;top:15px;font-size:23px;font-weight:500;color:#555;letter-spacing:-.5px}
.main-nav{right:66px;top:24px;display:flex;gap:18px;font-size:10.5px;color:#444}
.main-nav .active{color:var(--green);position:relative}
.main-nav .active::after{content:"";position:absolute;left:-2px;right:-2px;top:30px;height:2px;background:var(--green)}
.sub-nav{left:0;top:92px;width:812px;height:34px;background:var(--soft);border-top:1px solid #ddd;font-size:10.5px;color:#555;display:flex;justify-content:center;align-items:center;gap:7px}
.sub-nav .sep{color:#aaa}
.hero{left:0;top:126px;width:812px;height:318px;background:linear-gradient(100deg,#e4ecf3 0%,#cddbe8 35%,#b8c9d8 70%,#9fb2c4 100%)}
.hero-title{left:78px;top:192px;font-size:34px;font-weight:300;line-height:40px;color:#3c4650}
.hero-title span{color:var(--green)}
.hero-sub{left:79px;top:280px;font-size:14px;color:#1c1c1c}
.btn-signup{left:79px;top:317px;width:97px;height:34px;background:linear-gradient(#4d9a3a,#357a25);border:1px solid #2b6a1f;border-radius:3px;color:#fff;font-size:14.5px;line-height:32px;text-align:center}
.slider-dots{left:81px;top:413px;display:flex;gap:6px}
.slider-dots i{width:10px;height:10px;border-radius:50%;background:#8d96a0;display:block}
.slider-dots i:first-child{background:#4c545c}
.product-tab{top:466px;width:120px;text-align:center;font-size:14.5px;color:#444}
.product-tab svg{display:block;margin:0 auto 14px}
.product-tab.active{color:var(--green)}
.tab-rail{left:71px;top:555px;width:671px;height:4px;background:var(--line)}
.tab-rail-active{left:71px;top:555px;width:119px;height:4px;background:var(--green)}
.tab-pointer{left:125px;top:559px;width:0;height:0;border-left:6px solid transparent;border-right:6px solid transparent;border-top:6px solid var(--green)}
.stat-card{left:104px;top:589px;width:158px;height:93px;border:1px solid #d6d6d6;box-shadow:0 1px 2px rgba(0,0,0,.08);background:#fff}
.stat-card .lbl{font-size:5px;color:#aaa}
.stat-card .big{font-size:12px;color:var(--green);font-weight:500}
.feature-copy{left:284px;top:587px;width:424px;font-size:9.6px;line-height:16.8px;color:#555;text-align:justify}
.divider{left:74px;top:710px;width:664px;height:1px;background:#ccc}
.testimonial{left:110px;top:734px;width:592px;text-align:center;font-family:"Crimson Text",serif;font-size:19px;line-height:24px;color:#555}
.testimonial q{quotes:"❝" "❞"}
.testimonial q::before,.testimonial q::after{font-size:9px;vertical-align:middle;margin:0 10px;color:#666}
.testimonial-source{left:0;top:793px;width:812px;text-align:center;font-size:13px;color:var(--green)}
.engage{left:0;top:834px;width:812px;height:140px;background:var(--soft)}
.engage h3{font-size:14.5px;font-weight:400;color:var(--green)}
.engage p{font-size:9px;line-height:14.5px;color:#444;margin-top:10px}
.mail-form{left:109px;top:920px;width:254px;height:32px;background:#fff;border:1px solid #ddd;border-radius:2px}
.mail-form span{position:absolute;left:13px;top:10px;font-size:9px;color:#999}
.mail-form b{position:absolute;right:3px;top:3px;width:74px;height:25px;background:linear-gradient(#6a6a6a,#4b4b4b);border-radius:2px;color:#fff;font-weight:400;font-size:10px;line-height:25px;text-align:center}
.engage-split{left:406px;top:846px;width:1px;height:118px;background:#c9c9c9}
.social{top:923px;width:24px;height:24px;border-radius:2px}
.footer-col{top:996px}
.footer-col h4{font-size:12px;line-height:14px;height:14px;font-weight:400;color:var(--green);margin-bottom:10px}
.footer-col li{list-style:none;font-size:9.3px;line-height:17px;color:#444}
.badge{left:563px;top:1066px;width:25px;height:46px;background:#c73a25}
.call-box{left:601px;top:1068px;width:131px;height:42px;border-top:1px solid #777;border-bottom:1px solid #777;text-align:center;font-family:"Crimson Text",serif;color:#333}
.call-box .t{font-size:14px;letter-spacing:.5px;margin-top:5px}
.call-box .n{font-family:"Ubuntu",sans-serif;font-size:12.5px;line-height:14px}
.bottom-bar{left:0;top:1136px;width:812px;height:64px;background:var(--dark);color:#bbb;font-size:9px;text-align:center}
.bottom-bar nav{margin-top:15px;display:flex;justify-content:center;gap:6px}
.bottom-bar nav .sep{color:#777}
.bottom-bar small{display:block;margin-top:13px;font-size:9px}
</style>
</head>
<body>

<div class="abs promo-bar">Hi, I'm a Tolvix. Get one for your website <b>FREE!</b></div>
<div class="abs promo-close">×</div>

<header class="abs site-header">
  <div class="abs brand">brelvox!</div>
  <nav class="abs main-nav">
    <span class="active">Home</span><span>Features</span><span>Plugins</span><span>Widgets</span><span>Free SEO Tools</span>
  </nav>
</header>

<nav class="abs sub-nav">
  <span>Login</span><span class="sep">|</span><span>New Account</span><span class="sep">|</span><span>Privacy &amp; Security</span><span class="sep">|</span><span>Support</span>
</nav>

<section class="abs hero" role="img" aria-label="Photo of a cheering businessman sitting cross-legged on a rock with a laptop, against a pale misty mountain sky"></section>
<h1 class="abs hero-title">Is your website<br><span>Moving up?</span></h1>
<p class="abs hero-sub">Website analytics and SEO Tools</p>
<div class="abs btn-signup">Free Signup</div>
<div class="abs slider-dots"><i></i><i></i><i></i><i></i></div>

<div class="abs product-tab active" style="left:74px">
  <svg width="40" height="40" viewBox="0 0 40 40"><rect x="2" y="2" width="2" height="36" fill="#3f8f2f"/><rect x="2" y="36" width="36" height="2" fill="#3f8f2f"/><rect x="6" y="4" width="7" height="32" fill="#3f8f2f"/><rect x="15" y="16" width="7" height="20" fill="#3f8f2f"/><rect x="24" y="24" width="7" height="12" fill="#3f8f2f"/><rect x="31" y="28" width="7" height="8" fill="#3f8f2f"/></svg>
  Analytics
</div>
<div class="abs product-tab" style="left:209px">
  <svg width="40" height="40" viewBox="0 0 40 40"><circle cx="17" cy="17" r="11" fill="none" stroke="#555" stroke-width="5"/><path d="M25 25 L34 35" stroke="#555" stroke-width="6" stroke-linecap="round"/><rect x="13" y="16" width="2" height="5" fill="#555"/><rect x="16" y="13" width="2" height="8" fill="#555"/><rect x="19" y="15" width="2" height="6" fill="#555"/></svg>
  SEO
</div>
<div class="abs product-tab" style="left:342px">
  <svg width="40" height="40" viewBox="0 0 40 40"><path d="M3 3 H28 V22 H12 L6 28 V22 H3 Z" fill="#555"/><path d="M31 9 H37 V30 H34 V36 L28 30 H13 V25 H31 Z" fill="#555"/></svg>
  Live Chat
</div>
<div class="abs product-tab" style="left:478px">
  <svg width="40" height="40" viewBox="0 0 40 40"><path d="M6 26 V20 A14 14 0 0 1 34 20 V26" fill="none" stroke="#555" stroke-width="3.5"/><rect x="4" y="23" width="7" height="14" rx="2" fill="#555"/><rect x="29" y="23" width="7" height="14" rx="2" fill="#555"/></svg>
  Support Tickets
</div>
<div class="abs product-tab" style="left:612px">
  <svg width="40" height="40" viewBox="0 0 40 40"><polyline points="2,24 10,18 18,22 26,12 30,15 38,4" fill="none" stroke="#555" stroke-width="2"/><polyline points="2,36 10,30 18,34 26,26 30,30 38,24" fill="none" stroke="#555" stroke-width="2"/></svg>
  Heat Maps
</div>

<div class="abs tab-rail"></div>
<div class="abs tab-rail-active"></div>
<div class="abs tab-pointer"></div>

<div class="abs stat-card">
  <div class="abs lbl" style="left:10px;top:9px">Inquiries</div>
  <svg class="abs" style="left:10px;top:18px" width="92" height="20" viewBox="0 0 92 20">
    <g fill="#3f8f2f">
      <rect x="0" y="10" width="4" height="10"/><rect x="8" y="6" width="4" height="14"/><rect x="16" y="11" width="4" height="9"/><rect x="24" y="4" width="4" height="16"/><rect x="32" y="8" width="4" height="12"/><rect x="40" y="2" width="4" height="18"/><rect x="48" y="9" width="4" height="11"/><rect x="56" y="5" width="4" height="15"/><rect x="64" y="11" width="4" height="9"/><rect x="72" y="3" width="4" height="17"/><rect x="80" y="7" width="4" height="13"/><rect x="88" y="4" width="4" height="16"/>
    </g>
  </svg>
  <div class="abs lbl" style="left:11px;top:40px;letter-spacing:3.2px">JFMAMJJASOND</div>
  <div class="abs big" style="left:114px;top:20px">+142</div>
  <div class="abs lbl" style="left:114px;top:37px">FROM LAST YEAR</div>
  <div class="abs lbl" style="left:10px;top:62px">Gross Revenue</div>
  <div class="abs big" style="left:10px;top:70px">9,362.74</div>
  <div class="abs lbl" style="left:90px;top:62px">Net Revenue</div>
  <div class="abs big" style="left:90px;top:70px">6,734.89</div>
</div>

<p class="abs feature-copy">Sed imperdiet aliquam hendrerit. Aliquam tempor vel magna a aliquam. Cras vel elit leo. Morbi a aliquam dui. Donec gravida interdum vehicula. Fusce interdum erat id tortor rhoncus, at porta magna tincidunt. Etiam placerat erat vitae posuere suscipit. Vestibulum sed dolor sed odio eleifend aliquet. Phasellus nec quam sed leo malesuada volutpat. Vivamus urna libero, ultricies vel imperdiet nec, malesuada non nisi. In eu libero in risus convallis feugiat. Morbi eget nibh quam. Vivamus id eros vel sapien congue commodo quis sed odio.</p>

<div class="abs divider"></div>

<blockquote class="abs testimonial"><q>Your organization can never get enough reporting and research about effectiveness online!</q></blockquote>
<div class="abs testimonial-source">Pewbright.com</div>

<section class="abs engage">
  <div class="abs" style="left:108px;top:24px;width:270px">
    <h3>Join our Mailing List</h3>
    <p>We want you! Well, we want you to stay up to date with all the Brelvox! going ons.. Sign up now!</p>
  </div>
  <div class="abs" style="left:446px;top:24px;width:258px">
    <h3>Have an Idea or Gripe?</h3>
    <p style="text-align:justify">Were always looking to know how were doing. If you have ideas, tips or problems with our service, please let us know!</p>
  </div>
</section>
<div class="abs mail-form"><span>Enter your Mail ID</span><b>Sign up Now</b></div>
<div class="abs engage-split"></div>
<div class="abs social" style="left:449px;background:#3b5a9a"></div>
<div class="abs social" style="left:485px;background:#4fb4e6"></div>
<div class="abs social" style="left:522px;background:#1f75ab"></div>
<div class="abs social" style="left:558px;background:#ee7d24"></div>
<div class="abs social" style="left:594px;background:#d9443a"></div>

<div class="abs footer-col" style="left:79px">
  <h4>Site Links</h4>
  <ul><li>Home</li><li>Sign Up</li><li>My Account</li><li>Privacy &amp; Security</li><li>Feedback</li><li>Tell a Friend</li></ul>
</div>
<div class="abs footer-col" style="left:178px">
  <h4>Features</h4>
  <ul><li>Web Stats</li><li>Traffic Trend Analysis</li><li>Referring Keywords</li><li>Recent Visitor Locations</li><li>Recent Visitor Map</li><li>Actions &amp; Goals</li></ul>
</div>
<div class="abs footer-col" style="left:306px">
  <h4></h4>
  <ul><li>Heat Maps</li><li>Inbound Link Monitoring</li><li>Zumbek Rankmark Tracking</li><li>Vendra Rank Tracking</li><li>Keyword Research</li><li>Keyword Position Tracking</li></ul>
</div>
<div class="abs footer-col" style="left:449px">
  <h4>Free Tools</h4>
  <ul><li>WebStats Live</li><li>Site Analyzer</li><li>Rankmark Badges</li><li>SEO Optimizer</li><li>Web Thumbs</li><li>Bulk Domain Analyzer</li></ul>
</div>
<div class="abs footer-col" style="left:563px">
  <h4></h4>
  <ul><li>Tag Clouds</li><li>Link &amp; Site Diagnosis</li></ul>
</div>
<div class="abs badge"></div>
<div class="abs call-box">
  <div class="t">CALL TOLL FREE</div>
  <div class="n"><svg width="10" height="10" viewBox="0 0 10 10" style="vertical-align:-1px;margin-right:4px"><path d="M2 0 L4 2.5 L3 4 Q4.5 6 6 7 L7.5 6 L10 8 L8.5 10 Q2 9 0 1.5 Z" fill="#333"/></svg>888-555-0142</div>
</div>

<footer class="abs bottom-bar">
  <nav><span>Home</span><span class="sep">|</span><span>Features</span><span class="sep">|</span><span>Plugins</span><span class="sep">|</span><span>Widgets</span><span class="sep">|</span><span>Free SEO Tools</span><span class="sep">|</span><span>Business Inquiries</span><span class="sep">|</span><span>Feedback</span><span class="sep">|</span><span>Privacy</span><span class="sep">|</span><span>Tell a Friend</span></nav>
  <small>Copyright © 2013 Brelvox. All rights reserved.</small>
</footer>

</body>
</html>
```